BKT Consulting

Government/Entitlement Consulting Services- I assist developers obtain entitlements from local, state and federal government agencies so that they can build their projects. Often these projects are very complicated and political and may face community opposition.

Target Market(s)

Real Estate Developers

Industry/Entity Type

Business Consultant

Contact Information for Business Card

Dana Velmonte
Principal

Font styles to use
Serif
Sans Serif

Requirements
Must have
• Classy and professional appeal.
Nice to have
• I like a combination of a mat and glossy finish. I've seen that done with black and then a bold color for a pop, but am not 100% committed to that.

```html
<!DOCTYPE html>
<html lang="en">
<head>
<meta charset="utf-8">
<title>BKT Consulting – Business Card</title>
<link rel="stylesheet" href="https://fonts.googleapis.com/css2?family=Arimo:wght@400&display=swap">
<style>
  :root {
    --backdrop: #e9e7e3;
    --card: #ffffff;
    --card-shade: #ececec;
    --ink: #111111;
    --ink-soft: #2a2a2a;
    --icon-fill: #1a1a1a;
  }
  * { margin: 0; padding: 0; box-sizing: border-box; }
  html, body {
    width: 1200px; height: 858px; overflow: hidden;
    background: var(--backdrop);
    font-family: "Arimo", Arial, sans-serif;
    color: var(--ink);
  }
  .sheet {
    width: 1200px; height: 858px;
    display: flex; align-items: center; justify-content: center; gap: 60px;
  }
  .card {
    position: relative;
    width: 525px; height: 300px;
    background: radial-gradient(ellipse at 55% 45%, var(--card) 55%, var(--card-shade) 100%);
    box-shadow: 0 2px 0 #d4d4d4, 0 4px 0 #c9c9c9, 0 10px 24px rgba(0,0,0,.18);
  }
  /* Front */
  .front .brand-panel {
    position: absolute; left: 0; top: 0;
    width: 300px; height: 300px;
    display: flex; align-items: center; justify-content: center;
    padding-right: 10px;
  }
  .front .wordmark {
    font-size: 32px; letter-spacing: -0.2px; white-space: nowrap;
  }
  .front .divider {
    position: absolute; left: 300px; top: 22px;
    width: 1.5px; height: 256px; background: var(--ink-soft);
  }
  .front .identity {
    position: absolute; left: 324px; top: 54px;
  }
  .identity .name { font-size: 14px; }
  .identity .role { font-size: 11.5px; margin-top: 4px; color: var(--ink-soft); }
  .front .contacts {
    position: absolute; left: 324px; top: 150px;
    list-style: none; font-size: 13.5px;
  }
  .contacts li { display: flex; align-items: center; gap: 10px; height: 26px; white-space: nowrap; }
  .contacts svg { width: 14px; height: 14px; flex: none; }
  /* Back */
  .back .wordmark {
    position: absolute; inset: 0;
    display: flex; align-items: center; justify-content: center;
    font-size: 50px; letter-spacing: -0.3px;
  }
</style>
</head>
<body>
<main class="sheet">
  <section class="card front" aria-label="Card front">
    <div class="brand-panel">
      <div class="wordmark">BKT Consulting</div>
    </div>
    <div class="divider"></div>
    <div class="identity">
      <div class="name">Dana Velmonte</div>
      <div class="role">Principal</div>
    </div>
    <ul class="contacts">
      <li>
        <svg viewBox="0 0 14 14" aria-hidden="true"><rect width="14" height="14" fill="var(--icon-fill)"/><path d="M4 3h2l1 2.5-1.2.8a6 6 0 0 0 2 2l.8-1.2L11 8v2a1 1 0 0 1-1 1A7 7 0 0 1 3 4a1 1 0 0 1 1-1z" fill="#fff"/></svg>
        <span>555-014-2290</span>
      </li>
      <li>
        <svg viewBox="0 0 14 14" aria-hidden="true"><rect width="14" height="14" fill="var(--icon-fill)"/><circle cx="7" cy="7" r="4" fill="none" stroke="#fff" stroke-width="1"/><ellipse cx="7" cy="7" rx="1.8" ry="4" fill="none" stroke="#fff" stroke-width="0.8"/><line x1="3" y1="7" x2="11" y2="7" stroke="#fff" stroke-width="0.8"/></svg>
        <span>www.bktconsulting.com</span>
      </li>
      <li>
        <svg viewBox="0 0 14 14" aria-hidden="true"><rect width="14" height="14" fill="var(--icon-fill)"/><rect x="3" y="4" width="8" height="6" fill="none" stroke="#fff" stroke-width="1"/><path d="M3 4l4 3.2L11 4" fill="none" stroke="#fff" stroke-width="1"/></svg>
        <span>dana@bktconsulting.com</span>
      </li>
    </ul>
  </section>
  <section class="card back" aria-label="Card back">
    <div class="wordmark">BKT Consulting</div>
  </section>
</main>
</body>
</html>
```